Vehicle Wrap Design for Air Conditioning Brand - Tall Oak Vent

We are looking to re-brand our client's wrap design. The company is called Tall Oak Vent

TallOakVent.com
888-OAK-VENT

We are looking for a simple design with that features a Polar Bear to represent TALL OAK. We are interested in keeping a color scheme of blues and white -- we are open to pops of color such as neon yellow or orange.

The primary purpose of the wrap is for BRAND AWARENESS. The website and phone number should be present and simple to read.

Please submit your design mocked up on the attached van image.

Images of other vehicle wraps that we think look pretty good. Large, featured graphics of the characeture/logo, visible and simple to read context like phone/website

We don't have a logo, but we've attached some examples of Polar Bear logos from Pixelborough that we like. We're looking for this style illustration for our polar bear

Target Market(s)

Consumers that need AC service for their homes

Industry/Entity Type

HVAC (Air Conditioning and Heating)

Font styles to use
Sans Serif

Colors
0094D4
00A9DD
6FCCEA
C7EBF8
E9F6FB

Requirements
Must have
• Polar Bear logo to represent Tall Oak Vent, Business Name, Phone, Website
Nice to have
• Visually appealing, clean, simple graphics that grab attention but make the company name and number easy to read

```html
<!DOCTYPE html>
<html lang="en">
<head>
<meta charset="utf-8">
<title>Tall Oak Vent — Vehicle Wrap Artwork</title>
<link rel="stylesheet" href="https://fonts.googleapis.com/css2?family=Passion+One:wght@400;700&family=Roboto+Condensed:wght@700&family=Parisienne&display=swap">
<style>
  :root {
    --brand-blue: #0a79bd;
    --brand-sky: #00a9dd;
    --brand-ice: #c7ebf8;
    --brand-frost: #e9f6fb;
    --paper: #ffffff;
    --ink: #111111;
  }
  html, body {
    margin: 0;
    padding: 0;
    width: 1200px;
    height: 1000px;
    overflow: hidden;
    background: var(--paper);
  }
  .wrap-canvas {
    display: block;
    width: 1200px;
    height: 1000px;
  }
  .wrap-band { fill: var(--brand-blue); }
  .mascot-area { fill: url(#mascotTone); }
  .brand-name {
    font-family: "Passion One", sans-serif;
    font-weight: 700;
    fill: var(--brand-blue);
  }
  .contact-line {
    font-family: "Roboto Condensed", sans-serif;
    font-weight: 700;
    fill: var(--brand-blue);
  }
  .door-call {
    font-family: "Parisienne", cursive;
    fill: var(--ink);
  }
  .door-name {
    font-family: "Passion One", sans-serif;
    font-weight: 700;
    fill: var(--brand-blue);
  }
  .door-mascot { fill: url(#doorTone); }
</style>
</head>
<body>
<svg class="wrap-canvas" viewBox="0 0 1200 1000" xmlns="http://www.w3.org/2000/svg">
  <defs>
    <linearGradient id="mascotTone" x1="0" y1="0" x2="1" y2="1">
      <stop offset="0" stop-color="#ffffff"/>
      <stop offset="1" stop-color="#c7ebf8"/>
    </linearGradient>
    <linearGradient id="doorTone" x1="0" y1="0" x2="1" y2="1">
      <stop offset="0" stop-color="#00a9dd"/>
      <stop offset="1" stop-color="#0a79bd"/>
    </linearGradient>
  </defs>

  <!-- Side panel graphic -->
  <g class="side-panel">
    <path class="wrap-band" d="M320,120 H1100 V185
      C1060,215 1020,170 980,195 C940,220 900,170 860,195
      C820,220 780,170 740,195 C700,220 660,175 620,200
      C590,215 560,215 540,235 C500,290 500,520 540,560
      C580,540 620,520 660,545 C700,570 740,510 780,535
      C820,560 860,510 900,530 C940,550 980,510 1020,525
      C1060,540 1090,520 1100,500 V640 H320 Z"/>

    <rect class="mascot-area" x="335" y="210" width="190" height="330" rx="60"
          role="img" aria-label="Polar bear mascot illustration with snowy mountain peaks along the bands"/>

    <text class="brand-name" x="560" y="345" font-size="84" textLength="520" lengthAdjust="spacingAndGlyphs">TALL OAK VENT</text>
    <text class="contact-line" x="560" y="420" font-size="42" textLength="520" lengthAdjust="spacingAndGlyphs">(555) 214-0387  TallOakVent.com</text>
  </g>

  <!-- Door graphic -->
  <g class="door-panel">
    <rect class="door-mascot" x="80" y="440" width="95" height="52" rx="22"
          role="img" aria-label="Small cartoon car character"/>
    <text class="door-call" x="188" y="480" font-size="38">Call us</text>
    <text class="door-name" x="80" y="540" font-size="40" textLength="230" lengthAdjust="spacingAndGlyphs">TALL OAK VENT</text>
  </g>
</svg>
</body>
</html>
```